Facebook/ Instagram/ LinkedIn

Looking for profile images, banner images and templates for posting to instagram.

1. Profile and banner logo image for all three platforms
2. Pinned logo to go across three posts on instagram
3. Multiple backgrounds/ templates for instagram
4. Various images with logo for instagram

```html
<!DOCTYPE html>
<html lang="en">
<head>
<meta charset="utf-8">
<title>VENTA – Facebook Set</title>
<link href="https://fonts.googleapis.com/css2?family=Lato:wght@400;700;900&family=Ubuntu:wght@500;700&display=swap" rel="stylesheet">
<style>
  :root{
    --sheet:#d6d6d6;
    --ink:#111111;
    --sky:#00c8fb;
    --sky-deep:#00b4ea;
    --leaf:#8dc63f;
    --leaf-soft:#c6e08a;
    --paper:#ffffff;
    --slate:#555555;
  }
  *{margin:0;padding:0;box-sizing:border-box}
  html,body{width:775px;height:1200px;overflow:hidden;background:var(--sheet)}
  .sheet{position:relative;width:775px;height:1200px;font-family:"Lato",sans-serif;color:var(--ink)}
  .sheet__title{position:absolute;top:44px;width:100%;text-align:center;font-weight:900;font-size:23px;letter-spacing:1.5px}
  .sheet__subtitle{position:absolute;top:76px;width:100%;text-align:center;font-weight:900;font-size:13.5px;letter-spacing:1px}
  .label{position:absolute;font-weight:900;font-size:13.5px;letter-spacing:1px;text-align:center}
  .label--num{width:184px}
  .label--cover{left:0;width:775px}

  .post{position:absolute;width:184px;height:184px;overflow:hidden}
  .post--white{background:var(--paper)}
  .post--sky{background:var(--sky)}
  .post--leaf{background:linear-gradient(135deg,var(--leaf-soft),var(--leaf))}
  .backdrop{position:absolute;left:0;top:0;width:136px;height:100%}
  .post--white .backdrop,.cover .backdrop{background:linear-gradient(160deg,rgba(198,224,138,.35),rgba(198,224,138,.18))}
  .post--sky .backdrop{background:linear-gradient(160deg,rgba(0,150,220,.22),rgba(0,150,220,.08))}
  .post--leaf .backdrop{background:linear-gradient(160deg,rgba(110,160,40,.25),rgba(110,160,40,.05))}

  .brand{position:absolute;text-align:center;font-family:"Ubuntu",sans-serif}
  .brand__name{display:block;font-weight:700;line-height:1;letter-spacing:1px}
  .brand__line{display:block;font-weight:500;color:var(--slate);white-space:nowrap}
  .brand__division{display:flex;align-items:center;gap:4px;font-weight:500;color:var(--sky);white-space:nowrap}
  .brand__division::before,.brand__division::after{content:"";flex:1;height:1px;background:currentColor}
  .brand--light .brand__name,.brand--light .brand__line,.brand--light .brand__division{color:var(--paper)}
  .brand--light .brand__name{color:var(--paper)}
  .brand--sky .brand__name{color:var(--sky)}

  .post .brand{left:31px;width:124px}
  .post .brand__name{font-size:37px}
  .post .brand__line{font-size:8.2px;margin-top:3px}
  .post .brand__division{font-size:6px;margin-top:1px}

  .web-band{position:absolute;left:0;width:100%;display:flex;align-items:center;justify-content:center;font-family:"Lato",sans-serif;font-weight:700;letter-spacing:3px}
  .post .web-band{top:158px;height:14px;font-size:6.5px}
  .web-band--sky{background:var(--sky);color:var(--paper)}
  .web-band--white{background:var(--paper);color:var(--sky)}
  .web-band--white.leafy{color:var(--leaf)}
  .web-plain{position:absolute;left:0;width:100%;text-align:center;font-weight:700;font-size:6.5px;letter-spacing:3px;color:var(--sky)}
  .web-plain--light{color:var(--paper)}
  .wave{position:absolute;left:0;top:0;width:100%;height:100%}

  .cover{position:absolute;left:76px;width:617px;height:235px;background:var(--paper);overflow:hidden}
  .cover .backdrop{width:213px}
  .cover .brand__line{font-size:17.5px;margin-top:5px}
  .cover .brand__division{font-size:12.5px;gap:8px;margin-top:1px}
  .cover .web-band{left:213px;width:404px;top:189px;height:25px;font-weight:400;font-size:14px}
  .cover__web{position:absolute;left:393px;top:198px;color:var(--paper);font-size:12px;letter-spacing:1.5px}
</style>
</head>
<body>
<main class="sheet">
  <h1 class="sheet__title">FACEBOOK</h1>
  <h2 class="sheet__subtitle">SQUARE POSTS: 1080 X 1080 PIXELS</h2>

  <!-- Row one -->
  <section class="post post--white" style="left:76px;top:113px">
    <div class="backdrop" role="img" aria-label="Faint tower block illustration"></div>
    <div class="brand brand--sky" style="top:62px"><span class="brand__name">VENTA</span><span class="brand__line">Commercial Air Conditioning</span><span class="brand__division">A Division of Harlow Air</span></div>
    <div class="web-band web-band--sky">WWW.VENTA.COM.AU</div>
  </section>
  <section class="post post--sky" style="left:293px;top:113px">
    <div class="backdrop" role="img" aria-label="Faint tower block illustration"></div>
    <div class="brand brand--light" style="top:62px"><span class="brand__name">VENTA</span><span class="brand__line">Commercial Air Conditioning</span><span class="brand__division">A Division of Harlow Air</span></div>
    <div class="web-band web-band--white">WWW.VENTA.COM.AU</div>
  </section>
  <section class="post post--leaf" style="left:509px;top:113px">
    <div class="backdrop" role="img" aria-label="Faint tower block illustration"></div>
    <div class="brand brand--light" style="top:62px"><span class="brand__name">VENTA</span><span class="brand__line">Commercial Air Conditioning</span><span class="brand__division">A Division of Harlow Air</span></div>
    <div class="web-band web-band--white leafy">WWW.VENTA.COM.AU</div>
  </section>
  <div class="label label--num" style="left:76px;top:306px">01</div>
  <div class="label label--num" style="left:293px;top:306px">02</div>
  <div class="label label--num" style="left:509px;top:306px">03</div>

  <!-- Row two -->
  <section class="post post--white" style="left:76px;top:334px">
    <div class="backdrop" role="img" aria-label="Faint tower block illustration"></div>
    <div class="brand brand--sky" style="top:52px"><span class="brand__name">VENTA</span><span class="brand__line">Commercial Air Conditioning</span><span class="brand__division">A Division of Harlow Air</span></div>
    <svg class="wave" viewBox="0 0 184 184" aria-hidden="true">
      <path d="M0,132 C40,150 75,160 105,152 C135,144 160,136 184,150 L184,184 L0,184Z" fill="var(--sky)"/>
      <path d="M14,138 C60,163 110,158 150,138 C162,133 170,136 174,143 C150,134 110,150 70,155 C45,158 28,150 14,138Z" fill="var(--leaf)"/>
    </svg>
    <div class="web-plain web-plain--light" style="top:166px">WWW.VENTA.COM.AU</div>
  </section>
  <section class="post post--sky" style="left:293px;top:334px">
    <div class="backdrop" role="img" aria-label="Faint tower block illustration"></div>
    <div class="brand brand--light" style="top:61px"><span class="brand__name">VENTA</span><span class="brand__line">Commercial Air Conditioning</span><span class="brand__division">A Division of Harlow Air</span></div>
    <svg class="wave" viewBox="0 0 184 184" aria-hidden="true">
      <path d="M0,132 C40,150 75,160 105,152 C135,144 160,136 184,150 L184,184 L0,184Z" fill="var(--paper)"/>
      <path d="M14,138 C60,163 110,158 150,138 C162,133 170,136 174,143 C150,134 110,150 70,155 C45,158 28,150 14,138Z" fill="var(--leaf)"/>
    </svg>
    <div class="web-plain" style="top:166px">WWW.VENTA.COM.AU</div>
  </section>
  <section class="post post--leaf" style="left:509px;top:334px">
    <div class="backdrop" role="img" aria-label="Faint tower block illustration"></div>
    <div class="brand brand--light" style="top:61px"><span class="brand__name">VENTA</span><span class="brand__line">Commercial Air Conditioning</span><span class="brand__division">A Division of Harlow Air</span></div>
    <svg class="wave" viewBox="0 0 184 184" aria-hidden="true">
      <path d="M0,132 C40,150 75,160 105,152 C135,144 160,136 184,150 L184,184 L0,184Z" fill="var(--paper)"/>
      <path d="M14,138 C60,163 110,158 150,138 C162,133 170,136 174,143 C150,134 110,150 70,155 C45,158 28,150 14,138Z" fill="var(--sky)"/>
    </svg>
    <div class="web-plain" style="top:166px">WWW.VENTA.COM.AU</div>
  </section>
  <div class="label label--num" style="left:76px;top:539px">04</div>
  <div class="label label--num" style="left:293px;top:539px">05</div>
  <div class="label label--num" style="left:509px;top:539px">06</div>

  <!-- Cover one -->
  <section class="cover" style="top:578px">
    <div class="backdrop" role="img" aria-label="Faint tower block illustration"></div>
    <div class="brand brand--sky" style="left:274px;width:268px;top:44px"><span class="brand__name" style="font-size:84px">VENTA</span><span class="brand__line">Commercial Air Conditioning</span><span class="brand__division">A Division of Harlow Air</span></div>
    <div class="web-band web-band--sky">WWW.VENTA.COM.AU</div>
  </section>
  <div class="label label--cover" style="top:838px">FACEBOOK COVER: 820 X 312 PIXELS_01</div>

  <!-- Cover two -->
  <section class="cover" style="top:876px">
    <div class="backdrop" role="img" aria-label="Faint tower block illustration"></div>
    <div class="brand brand--sky" style="left:288px;width:242px;top:16px"><span class="brand__name" style="font-size:76px">VENTA</span><span class="brand__line" style="font-size:16px">Commercial Air Conditioning</span><span class="brand__division" style="font-size:11.5px">A Division of Harlow Air</span></div>
    <svg class="wave" viewBox="0 0 617 235" aria-hidden="true">
      <path d="M0,154 C80,200 170,226 270,212 C390,194 500,168 617,200 L617,235 L0,235Z" fill="var(--sky)"/>
      <path d="M52,172 C150,206 250,200 350,170 C440,145 520,140 588,176 C520,154 440,160 360,182 C260,208 150,212 52,172Z" fill="var(--leaf)"/>
    </svg>
    <div class="cover__web">WWW.VENTA.COM.AU</div>
  </section>
  <div class="label label--cover" style="top:1135px">FACEBOOK COVER: 820 X 312 PIXELS_02</div>
</main>
</body>
</html>
```